High End Notary Service Business Card Design

Want a professional and elegant/luxurious business card that is clean and simple in the design. A notary is a trusted professional that helps people sign very important documents. The card should be in alignment with this service provided.

Most of the time, service will be for the purchase of a home or refinance of a mortgage

There is NO LOGO. This is aesthetic. A look and feel. Conveying professionalism and concierge level of service.

Target Market(s)

Other business professionals, Lawyers, Escrow Officers, Loan Officers

Industry/Entity Type

Legal

Contact Information for Business Card

This will be a one-sided business card

Colors
35a7d7
3176b5
85cae6
d3a5cc
b868aa
ffffff
0356a4

Requirements
Must have
• Doreen L. Marsh-Whitlock
Notary Public

614-872-3916
MarshPublicNotary@Vornmail.com
Nice to have
• Headshot photo below. Convey the aspect of signing documents. No black cards. Preference is shades of blue: light blue, navy, aqua, gold, white, or lavendar, etc.
Should not have
• No scales or legal scales.

```html
<!DOCTYPE html>
<html lang="en">
<head>
<meta charset="utf-8">
<title>Doreen L. Marsh-Whitlock — Notary Public Business Card</title>
<link rel="stylesheet" href="https://fonts.googleapis.com/css2?family=Jost:wght@400&display=swap">
<style>
  :root {
    --backdrop: #f3f3f3;
    --navy: #1c2944;
    --gold: #c9a96e;
    --gold-soft: rgba(201, 169, 110, 0.55);
  }
  html, body {
    margin: 0;
    padding: 0;
    width: 1200px;
    height: 1200px;
    overflow: hidden;
    background: var(--backdrop);
  }
  .business-card {
    position: absolute;
    left: 222px;
    top: 384px;
    width: 756px;
    height: 431px;
    box-sizing: border-box;
    border: 9px solid var(--gold);
    background: var(--navy);
    font-family: "Jost", "Futura", sans-serif;
    color: var(--gold);
  }
  .dot-field {
    position: absolute;
    width: 217px;
    height: 53px;
    background: var(--gold-soft);
  }
  .dot-field--top { left: 39px; top: 68px; }
  .dot-field--bottom { left: 471px; top: 317px; }

  .identity {
    position: absolute;
    right: 52px;
    top: 42px;
    text-align: right;
  }
  .identity__name {
    display: flex;
    align-items: center;
    justify-content: flex-end;
    gap: 8px;
    font-size: 26px;
    line-height: 1;
    letter-spacing: 0.2px;
  }
  .quill-mark {
    display: block;
    width: 28px;
    height: 73px;
    background: linear-gradient(160deg, var(--gold), #a88a52);
    border-radius: 14px 14px 14px 14px / 30px 30px 40px 40px;
    transform: rotate(18deg);
  }
  .identity__title {
    margin-top: -6px;
    font-size: 23px;
    letter-spacing: 0.3px;
  }

  .contact {
    position: absolute;
    left: 39px;
    top: 307px;
    list-style: none;
    margin: 0;
    padding: 0;
    font-size: 24px;
    letter-spacing: 0.3px;
  }
  .contact__item {
    display: flex;
    align-items: center;
    gap: 14px;
    height: 39px;
  }
  .contact__icon {
    width: 29px;
    height: 27px;
    fill: var(--gold);
    flex: none;
  }
</style>
</head>
<body>
  <main class="business-card">
    <div class="dot-field dot-field--top" role="img" aria-label="Gold diamond dot pattern"></div>

    <header class="identity">
      <div class="identity__name">
        <span>Doreen L.</span>
        <span class="quill-mark" role="img" aria-label="Gold quill feather illustration"></span>
        <span>Marsh-Whitlock</span>
      </div>
      <div class="identity__title">Notary Public</div>
    </header>

    <ul class="contact">
      <li class="contact__item">
        <svg class="contact__icon" viewBox="0 0 24 24" aria-hidden="true">
          <path d="M6.6 10.8a15.1 15.1 0 0 0 6.6 6.6l2.2-2.2c.3-.3.7-.4 1-.2 1.1.4 2.3.6 3.6.6.6 0 1 .4 1 1V20c0 .6-.4 1-1 1A17 17 0 0 1 3 4c0-.6.4-1 1-1h3.5c.6 0 1 .4 1 1 0 1.2.2 2.4.6 3.6.1.3 0 .7-.2 1z"/>
        </svg>
        <span>614-872-3916</span>
      </li>
      <li class="contact__item">
        <svg class="contact__icon" viewBox="0 0 24 20" aria-hidden="true">
          <path d="M1 3.5 12 11 23 3.5V2.5C23 1.7 22.3 1 21.5 1h-19C1.7 1 1 1.7 1 2.5z"/>
          <path d="M1 5.8V17.5c0 .8.7 1.5 1.5 1.5h19c.8 0 1.5-.7 1.5-1.5V5.8L12 13.3z"/>
        </svg>
        <span>MarshPublicNotary@Vornmail.com</span>
      </li>
    </ul>

    <div class="dot-field dot-field--bottom" role="img" aria-label="Gold diamond dot pattern"></div>
  </main>
</body>
</html>
```